the letter head should have the logo ( may be top left), " Fenwick Ridge Institute" (may be top/middle ) and the two clinics info in a vertical column ( along the left side of the page )

Target Market(s)

other physicians and official letters

Requirements
Must have
• the info provided in the attachements

```html
<!DOCTYPE html>
<html lang="en">
<head>
<meta charset="utf-8">
<title>Fenwick Ridge Institute – Letterhead and Envelope</title>
<link href="https://fonts.googleapis.com/css2?family=Libre+Baskerville:wght@400;700&family=Arimo:wght@400&display=swap" rel="stylesheet">
<style>
  :root{
    --bg:#f2f2f2;
    --paper:#ffffff;
    --ink:#2f3b43;
    --accent:#9c2a6a;
    --body:#7a7a7a;
    --rule:#3a3a3a;
    --sign:#e6e6e6;
  }
  *{box-sizing:border-box;margin:0;padding:0}
  html,body{width:1200px;height:1200px;overflow:hidden}
  body{background:var(--bg);position:relative;font-family:"Arimo",Arial,sans-serif}
  .sprite{position:absolute;width:0;height:0}

  .sheet{position:absolute;background:var(--paper);box-shadow:0 1px 4px rgba(0,0,0,.18)}
  .letterhead{left:60px;top:40px;width:600px;height:800px}
  .envelope{left:510px;top:870px;width:650px;height:285px}

  .brand{position:absolute;display:flex;align-items:center;gap:10px}
  .brand-square{width:22px;height:22px;background:var(--ink);flex:none}
  .brand-name{font-family:"Libre Baskerville",Georgia,serif;font-weight:700;color:var(--ink);font-size:19px;line-height:1.15;letter-spacing:.5px}
  .letterhead .brand{left:0;right:0;top:44px;justify-content:center}
  .envelope .brand{left:20px;top:26px}
  .envelope .brand-name{font-size:16px}

  /* left-side clinic column */
  .clinic-column{position:absolute;left:22px;top:150px;bottom:40px;width:150px;display:flex;flex-direction:column;gap:26px}
  .column-rule{position:absolute;left:184px;top:150px;bottom:40px;width:1px;background:var(--rule)}

  /* letter content */
  .letter-main{position:absolute;left:208px;right:42px;top:150px;bottom:40px;display:flex;flex-direction:column;color:var(--body)}
  .subject{align-self:flex-end;font-size:14px;margin-top:26px}
  .greeting{font-size:15px;margin-top:24px}
  .letter-body{font-size:9.4px;line-height:1.28;text-align:justify;margin-top:14px}
  .letter-body p{margin-bottom:14px}
  .closing{font-size:14px;margin-top:40px}
  .signer{font-size:8.5px;margin-top:4px}
  .signature{width:90px;height:50px;background:var(--sign);border-radius:4px;margin-top:8px}

  .office{font-family:"Libre Baskerville",Georgia,serif;font-size:8.6px;color:var(--ink);line-height:1.6;font-style:normal}
  .office-title{color:var(--accent);font-weight:700;font-size:9px}
  .office-line{display:flex;align-items:flex-start;gap:4px}
  .office-line svg{width:8px;height:8px;fill:var(--accent);flex:none;margin-top:3px}

  .envelope .office{position:absolute;top:212px}
  .envelope .office--left{left:12px}
  .envelope .office--right{left:192px}
</style>
</head>
<body>
<svg class="sprite" aria-hidden="true">
  <symbol id="icon-phone" viewBox="0 0 10 10"><path d="M1 3.5C1 2 2.5 1.5 5 1.5S9 2 9 3.5L7.5 4.3 6.8 3.3H3.2L2.5 4.3ZM2.3 5h5.4l.8 3.5H1.5Z"/></symbol>
  <symbol id="icon-fax" viewBox="0 0 10 10"><path d="M3 1h4v2.5H3ZM1 4h8v3.5H7.5V6h-5v1.5H1ZM3 6.8h4V9H3Z"/></symbol>
  <symbol id="icon-pin" viewBox="0 0 10 10"><path d="M5 .5a3.3 3.3 0 0 0-3.3 3.3C1.7 6.3 5 9.5 5 9.5s3.3-3.2 3.3-5.7A3.3 3.3 0 0 0 5 .5Zm0 4.6a1.3 1.3 0 1 1 0-2.6 1.3 1.3 0 0 1 0 2.6Z"/></symbol>
</svg>

<section class="sheet letterhead">
  <div class="brand"><span class="brand-square"></span><span class="brand-name">Fenwick Ridge Institute</span></div>

  <aside class="clinic-column">
    <address class="office">
      <div class="office-title">Harlow Office</div>
      <div class="office-line"><svg><use href="#icon-phone"/></svg><span>555-310-4821</span></div>
      <div class="office-line"><svg><use href="#icon-fax"/></svg><span>555-310-4822</span></div>
      <div class="office-line"><svg><use href="#icon-pin"/></svg><span>2180 W. Alder St.<br>Harlow 40112</span></div>
    </address>
    <address class="office">
      <div class="office-title">Cedar Bend Office</div>
      <div class="office-line"><svg><use href="#icon-phone"/></svg><span>555-782-6093</span></div>
      <div class="office-line"><svg><use href="#icon-fax"/></svg><span>555-782-6094</span></div>
      <div class="office-line"><svg><use href="#icon-pin"/></svg><span>740 N. College Ave.<br>Suite 208, 40367</span></div>
    </address>
  </aside>
  <div class="column-rule"></div>

  <div class="letter-main">
    <div class="subject">SUB: ........................................</div>
    <div class="greeting">Dear Sir</div>
    <div class="letter-body">
      <p>Lorem Ipsum is simply dummy text of the printing and typesetting industry. Lorem Ipsum has been the industry's standard dummy text ever since the 1500s, when an unknown printer took a galley of type and scrambled it to make a type specimen book. It was popularised in the 1960s with the release of Letraset sheets containing Lorem Ipsum passages, and more recently with desktop publishing software like Aldus PageMaker including versions of Lorem Ipsum.</p>
      <p>It is a long established fact that a reader will be distracted by the readable content of a page when looking at its layout. The point of using Lorem Ipsum is that it has a more-or-less normal distribution of letters, as opposed to using 'Content here, content here', making it look like readable English. Many desktop publishing packages use it when looking for a model text.</p>
      <p>The point of using Lorem Ipsum is that it has a more-or-less normal distribution of letters, as opposed to using 'Content here, content here'. Many web page editors now use Lorem Ipsum as their default model text, and various versions have evolved over the years, sometimes by accident, sometimes on purpose, and the like. English. A search for 'lorem ipsum' will uncover many web sites still in their infancy.</p>
    </div>
    <div class="closing">Warm regards</div>
    <div class="signer">Daniel Hartley M.D.</div>
    <div class="signature" role="img" aria-label="Handwritten signature"></div>
  </div>
</section>

<section class="sheet envelope">
  <div class="brand"><span class="brand-square"></span><span class="brand-name">Fenwick Ridge Institute</span></div>
  <address class="office office--left">
    <div class="office-title">Harlow Office</div>
    <div class="office-line"><svg><use href="#icon-phone"/></svg><span>555-310-4821</span></div>
    <div class="office-line"><svg><use href="#icon-fax"/></svg><span>555-310-4822</span></div>
    <div class="office-line"><svg><use href="#icon-pin"/></svg><span>2180 W. Alder St. Harlow 40112</span></div>
  </address>
  <address class="office office--right">
    <div class="office-title">Cedar Bend Office</div>
    <div class="office-line"><svg><use href="#icon-phone"/></svg><span>555-782-6093</span></div>
    <div class="office-line"><svg><use href="#icon-fax"/></svg><span>555-782-6094</span></div>
    <div class="office-line"><svg><use href="#icon-pin"/></svg><span>740 N. College Ave. Suite 208,40367</span></div>
  </address>
</section>
</body>
</html>
```